NEW Modern Sleek Business Card for VR Language Startup

Our startup is using VR to lead the next wave of world language education. We need a two-sided business card that introduces the larger organization (Quorvel Language Inc) and our contact info on one side and shows the product, Lumidrasca, on the other side.

Side 1 (contact info)= Quorvel Logo and Contact info (name, title, phone, email)

Side 2 (product)= Lumidrasc logo, text, and website
Text= Culturally Immersive Language Learning Games
Website= www.lumidrasc.example

Target Market(s)

Education, Technology

Contact Information for Business Card

Contact info will be updated upon approval of the design. For now, put this as a placeholder.

Perry Hollins
Founder & CEO
phollins@mailtrove.example
(555)-014-2736

Font styles to use
Other font styles liked:
• Gibson and Century Gothic are the brand fonts

Requirements
Nice to have
• I would love to see cohesion between the design and colors of the two logos. I have attached a few business card designs that I like, so you can get a feel for my preferred style.

```html
<!DOCTYPE html>
<html lang="en">
<head>
<meta charset="utf-8">
<title>Quorvel Language — Business Card</title>
<link rel="stylesheet" href="https://fonts.googleapis.com/css2?family=Questrial&display=swap">
<style>
  :root {
    --page: #ffffff;
    --card: #263248;
    --text-light: #c9cdd4;
    --accent-cyan: #2fb5ea;
    --logo-blue: #3d8fe0;
    --wave-blue: #3f7fd6;
    --wave-magenta: #c2338f;
    --wave-orange: #f08a2c;
    --shadow: #e6e6e6;
  }
  * { margin: 0; padding: 0; box-sizing: border-box; }
  html, body { width: 1200px; height: 1000px; overflow: hidden; background: var(--page); }
  body { position: relative; font-family: "Questrial", "Century Gothic", sans-serif; }
  .card {
    position: absolute;
    width: 512px;
    height: 294px;
    background: var(--card);
    overflow: hidden;
  }
  .card-shadow {
    position: absolute;
    width: 512px;
    height: 12px;
    border-radius: 0 0 50% 50%;
    background: var(--shadow);
  }
  .card--product { left: 344px; top: 160px; }
  .card--contact { left: 345px; top: 517px; }
  .shadow--product { left: 344px; top: 454px; }
  .shadow--contact { left: 345px; top: 811px; }
  .wave-band { position: absolute; inset: 0; }
  .brand {
    position: absolute;
    display: flex;
    flex-direction: column;
    align-items: center;
    gap: 8px;
  }
  .brand-dot { width: 48px; height: 48px; border-radius: 50%; }
  .brand--product { left: 42px; top: 33px; }
  .brand--product .brand-dot { background: var(--logo-blue); }
  .brand--product .brand-name { font-size: 20px; color: var(--logo-blue); }
  .brand--contact { left: 56px; top: 134px; }
  .brand--contact .brand-dot { background: var(--logo-blue); width: 44px; height: 44px; }
  .brand--contact .brand-name { font-size: 21px; color: var(--text-light); letter-spacing: 2px; }
  .tagline {
    position: absolute;
    right: 44px;
    top: 148px;
    text-align: right;
    font-size: 23px;
    line-height: 29px;
    color: var(--text-light);
    text-transform: uppercase;
  }
  .website {
    position: absolute;
    right: 44px;
    top: 240px;
    font-size: 16px;
    color: var(--accent-cyan);
  }
  .contact-name {
    position: absolute;
    right: 45px;
    top: 60px;
    font-size: 40px;
    color: var(--text-light);
    white-space: nowrap;
  }
  .contact-title {
    position: absolute;
    right: 45px;
    top: 106px;
    font-size: 18px;
    color: var(--accent-cyan);
    text-transform: uppercase;
  }
  .contact-details {
    position: absolute;
    right: 45px;
    top: 176px;
    text-align: right;
    font-size: 15px;
    line-height: 22px;
    color: var(--text-light);
  }
</style>
</head>
<body>
  <section class="card card--product">
    <svg class="wave-band" width="512" height="294" viewBox="0 0 512 294" role="img" aria-label="Flowing line-wave pattern sweeping from lower left to upper right, blue to magenta to orange">
      <defs>
        <linearGradient id="band-product" x1="0" y1="1" x2="1" y2="0">
          <stop offset="0" stop-color="var(--wave-blue)" stop-opacity="0.15"/>
          <stop offset="0.55" stop-color="var(--wave-blue)" stop-opacity="0.4"/>
          <stop offset="0.8" stop-color="var(--wave-magenta)" stop-opacity="0.5"/>
          <stop offset="1" stop-color="var(--wave-orange)" stop-opacity="0.55"/>
        </linearGradient>
      </defs>
      <path d="M0 190 C120 120 260 60 495 0 L420 0 C250 50 110 170 80 294 L0 294 Z" fill="url(#band-product)"/>
    </svg>
    <div class="brand brand--product">
      <span class="brand-dot"></span>
      <span class="brand-name">Lumidrasc</span>
    </div>
    <p class="tagline">Culturally immersive<br>language learning<br>games</p>
    <p class="website">www.lumidrasc.example</p>
  </section>
  <div class="card-shadow shadow--product"></div>

  <section class="card card--contact">
    <svg class="wave-band" width="512" height="294" viewBox="0 0 512 294" role="img" aria-label="Flowing line-wave pattern sweeping from upper left to lower right, blue to magenta to orange">
      <defs>
        <linearGradient id="band-contact" x1="0" y1="0" x2="1" y2="1">
          <stop offset="0" stop-color="var(--wave-blue)" stop-opacity="0.15"/>
          <stop offset="0.45" stop-color="var(--wave-blue)" stop-opacity="0.4"/>
          <stop offset="0.75" stop-color="var(--wave-magenta)" stop-opacity="0.5"/>
          <stop offset="1" stop-color="var(--wave-orange)" stop-opacity="0.55"/>
        </linearGradient>
      </defs>
      <path d="M0 0 L110 0 C210 110 360 200 512 270 L512 294 L390 294 C250 200 110 130 0 70 Z" fill="url(#band-contact)"/>
    </svg>
    <h1 class="contact-name">Perry Hollins</h1>
    <p class="contact-title">Founder &amp; CEO</p>
    <div class="brand brand--contact">
      <span class="brand-dot"></span>
      <span class="brand-name">Quorvel</span>
    </div>
    <p class="contact-details">phollins@mailtrove.example<br>(555)-014-2736</p>
  </section>
  <div class="card-shadow shadow--contact"></div>
</body>
</html>
```